Design a book cover for "The Harvester's Ledger"

We need a book cover for a book titled "The Harvester's Ledger" The subtitle is "Why Machines Deliver a Shared Dividend, the Close of Levy Systems, and a Steady Treasury"
You can use one of the attached files of cover art, or come up with your own art - designer's choice!
Author's Name is Brent Hallow
We'd like the copy in the attached file "Back Cover" on the back cover, along with the copy in "About the Author" and the author's photo on the back cover.
Updates

Project Deadline Extended Reason: The deadline has been extended to give time for designers to respond to comments. Feel free to submit designs that do not use the cover art graphics attached to the brief - that art was meant as a suggestion. Added Sunday, January 15, 2017

Target Market(s)

Layperson

Font styles to use
Sans Serif

Colors
0456a4
3176b5
85abd2
0293ce
33a6d7
85cae6
1b1b1b
474747
919191

Requirements
Nice to have
• We'd like to see how the horse and rider would look on the front cover. The attached file, "Pendlewick Option", is a rough sketch. The artist is refining it, adding color, and will have the rider carrying modern technology instead of scrolls.
• We are open to all colors, but have indicated some colors we like.

```html
<!DOCTYPE html>
<html lang="en">
<head>
<meta charset="utf-8">
<title>The Harvester's Ledger — Book Cover</title>
<link rel="stylesheet" href="https://fonts.googleapis.com/css2?family=Bebas+Neue&family=Oswald:wght@300;500;600&family=Cinzel:wght@500&display=swap">
<style>
  :root {
    --stage: #86c6bd;
    --cover: #2a2736;
    --cover-deep: #221f2c;
    --trace: #3a3748;
    --accent: #e9f01c;
    --ink-light: #ffffff;
    --cloud: #eef0f2;
    --note: #2fae4f;
  }
  * { margin: 0; padding: 0; box-sizing: border-box; }
  html, body {
    width: 1200px;
    height: 1034px;
    overflow: hidden;
    background: var(--stage);
  }
  .book-cover {
    position: absolute;
    left: 280px;
    top: 37px;
    width: 640px;
    height: 960px;
    background: linear-gradient(160deg, var(--cover) 0%, var(--cover-deep) 100%);
    box-shadow: 0 18px 40px rgba(0, 0, 0, 0.25);
    overflow: hidden;
  }
  .circuit-texture {
    position: absolute;
    inset: 0;
    background:
      radial-gradient(ellipse at 30% 40%, rgba(90, 86, 110, 0.22), transparent 60%),
      radial-gradient(ellipse at 75% 70%, rgba(90, 86, 110, 0.18), transparent 55%);
  }
  .title {
    position: absolute;
    left: 48px;
    right: 48px;
    top: 56px;
    color: var(--accent);
    text-transform: uppercase;
  }
  .title-lead {
    display: block;
    font-family: "Oswald", sans-serif;
    font-weight: 600;
    font-size: 74px;
    line-height: 1;
    letter-spacing: 1px;
  }
  .title-main {
    position: relative;
    display: block;
    margin-top: 6px;
    font-family: "Bebas Neue", sans-serif;
    font-size: 190px;
    line-height: 0.9;
    letter-spacing: 10px;
    text-align: center;
  }
  .title-rules {
    position: absolute;
    left: 0;
    top: 0;
    width: 544px;
    height: 180px;
  }
  .cover-art {
    position: absolute;
    left: 150px;
    top: 360px;
    width: 340px;
    height: 300px;
    border-radius: 16px;
    background: radial-gradient(ellipse at 50% 40%, var(--cloud) 0%, #c9ccd2 38%, rgba(60, 58, 74, 0.6) 70%, transparent 100%);
  }
  .subtitle {
    position: absolute;
    left: 40px;
    right: 40px;
    top: 760px;
    font-family: "Oswald", sans-serif;
    font-weight: 500;
    font-size: 24px;
    line-height: 1.2;
    color: var(--accent);
    text-transform: uppercase;
    text-align: center;
    letter-spacing: -0.2px;
  }
  .author {
    position: absolute;
    left: 0;
    right: 0;
    top: 862px;
    font-family: "Cinzel", serif;
    font-weight: 500;
    font-size: 34px;
    color: var(--ink-light);
    text-align: center;
    letter-spacing: 3px;
  }
</style>
</head>
<body>
  <main class="book-cover">
    <div class="circuit-texture"></div>

    <h1 class="title">
      <span class="title-lead">The Harvester's</span>
      <span class="title-main">
        <svg class="title-rules" viewBox="0 0 544 180" aria-hidden="true">
          <g stroke="#e9f01c" stroke-width="2" fill="none">
            <polyline points="10,30 10,10 150,10"/>
            <polyline points="394,10 534,10 534,30"/>
            <line x1="40" y1="170" x2="200" y2="170"/>
            <line x1="344" y1="170" x2="504" y2="170"/>
          </g>
        </svg>
        Ledger
      </span>
    </h1>

    <div class="cover-art" role="img" aria-label="Illustration of a banknote with a dollar sign entering a white cloud, with rows of binary digits below"></div>

    <p class="subtitle">Why Machines Deliver a Shared Dividend<br>the Close of Levy Systems, and a Steady Treasury</p>

    <p class="author">BRENT HALLOW</p>
  </main>
</body>
</html>
```